Website Design for a "Talent Recruitment Agency"

We are looking for a website design for the website of our "Talent Recruitment Agency"; which is called "Crestway Hub".
Our recruitment website "Crestway Hub" will be focusing on: "Crestway Hub: Linking People & Firms in Switzerland"; which means our target audience is two-folded:
(i) TALENT - that is currently residing in- or outside of Switzerland, and is open for and interested in the "Swiss Job Market".
(ii) COMPANIES - that are looking for talent for specific job vacancies in Switzerland.
With our "Crestway Hub" approach we inted to focus on Membership & Partnership:
(a)"Membership"(TALENT)
and
(b)"Partnership"(COMPANIES)
Some of the competitor sites we like are:
• www.plimora42.dk
• www.qelvo.ch
• www.brandolix.ch/en
A sitemap example of our website is attached.
Also attached is a "Crestway Hub" logo in .eps format and one in .jpeg format.
We very much look forward to receive your creative ideas.
Best regards,
Crestway Hub
Crestway Hub: Linking People & Firms in Switzerland.
Website: crestwayhub.ch - Twitter: CrestwayHubCH
Target Market(s)
(i) TALENT (with around 0-10 years of working experience), currently residing in- or outside of Switzerland, but eligible to work in Switzerland.
(ii) COMPANIES (national or international) that are based in Switzerland.
Industry/Entity Type
Recruitment

```html
<!DOCTYPE html>
<html lang="en">
<head>
<meta charset="utf-8">
<title>Crestway Hub – Linking People &amp; Firms in Switzerland</title>
<link rel="stylesheet" href="https://fonts.googleapis.com/css2?family=Open+Sans:wght@400;600;700&family=Varela+Round&display=swap">
<style>
:root{
  --blue:#1b82c8;
  --blue-dark:#0b6fb3;
  --blue-band:#2a8cce;
  --blue-footer:#0c71b6;
  --blue-bottom:#075c97;
  --orange:#ee6a24;
  --grey-bg:#efefef;
  --grey-line:#dcdcdc;
  --text:#555;
  --white:#fff;
}
*{box-sizing:border-box;margin:0;padding:0}
html,body{width:1200px;height:2332px;overflow:hidden}
body{position:relative;background:var(--white);font-family:"Open Sans",Arial,sans-serif;color:var(--text)}
.abs{position:absolute}

/* header */
.site-header{position:absolute;left:0;top:0;width:1200px;height:148px;background:linear-gradient(#fafafa,#e9e9e9);border-top:6px solid var(--orange);border-bottom:1px solid #d2d2d2}
.brand{position:absolute;left:62px;top:58px;display:flex;align-items:center;gap:12px}
.brand-dot{width:46px;height:46px;border-radius:50%;background:var(--orange)}
.brand-name{font-family:"Varela Round","Open Sans",sans-serif;font-size:34px;color:var(--blue)}
.search{position:absolute;left:859px;top:13px;width:181px;height:27px;border:1px solid #c9c9c9;border-radius:14px;background:#fff;font-size:11px;color:#777;padding:6px 14px}
.search svg{position:absolute;right:10px;top:7px}
.language{position:absolute;left:1054px;top:16px;font-size:13px;color:#444}
.language .flag{display:inline-block;width:14px;height:14px;background:#e4252c;vertical-align:-2px;margin-left:6px;position:relative}
.language .flag::before,.language .flag::after{content:"";position:absolute;background:#fff}
.language .flag::before{left:6px;top:3px;width:2px;height:8px}
.language .flag::after{left:3px;top:6px;width:8px;height:2px}
.main-nav{position:absolute;top:76px;left:0;width:1200px;font-size:14px;letter-spacing:.5px;color:#555}
.main-nav a{position:absolute;color:inherit;text-decoration:none;transform:translateX(-50%);line-height:26px}
.main-nav a.active{background:var(--blue);color:#fff;padding:0 16px;border-radius:13px}

/* hero */
.hero-title{position:absolute;top:244px;left:0;width:1200px;text-align:center;font-family:"Varela Round","Open Sans",sans-serif;font-size:26px;letter-spacing:1.5px;color:var(--blue)}
.hero-title span{color:var(--orange)}
.hero-people{position:absolute;left:78px;top:300px;width:1025px;height:318px;background:linear-gradient(180deg,#fff 0%,#f4f6f9 30%,#cfdcea 70%,#b9c9db 100%)}

/* features */
.features{position:absolute;left:0;top:618px;width:1200px;height:676px;background:var(--grey-bg)}
.feature-grid-h{position:absolute;left:156px;top:92px;width:964px;height:1px;background:var(--grey-line)}
.feature-grid-h2{position:absolute;left:156px;top:344px;width:964px;height:1px;background:var(--grey-line)}
.feature-grid-v{position:absolute;left:598px;top:92px;width:1px;height:500px;background:var(--grey-line)}
.feature-icon{position:absolute;width:106px;height:106px;border-radius:50%;background:var(--blue);display:flex;align-items:center;justify-content:center}
.feature{position:absolute;width:330px}
.feature h3{font-size:15px;font-weight:400;color:var(--blue);letter-spacing:.5px;margin-bottom:8px}
.feature p{font-size:14px;line-height:20px;color:#666}
.btn-more{display:inline-block;margin-top:14px;width:108px;height:28px;line-height:28px;text-align:center;background:var(--orange);color:#fff;font-size:13px;border-bottom:2px solid #c8531a}
.feature-social{position:absolute;top:600px;left:556px;display:flex;gap:8px}
.dot{width:26px;height:26px;border-radius:50%;background:#2a5c9e}

/* content */
.section-heading{position:absolute;font-size:20px;letter-spacing:1px;color:var(--blue);font-weight:400}
.section-heading span{color:var(--orange)}
.rule{position:absolute;height:1px;background:#d5d5d5}
.welcome-text{position:absolute;left:84px;top:1430px;width:440px;font-size:14px;line-height:21px;color:#555}
.welcome-text p+p{margin-top:21px}
.job{position:absolute;left:628px;width:460px}
.job-thumb{position:absolute;left:0;top:0;width:129px;height:90px;border:3px solid #d4d4d4;background:linear-gradient(135deg,#f2f2f2,#b7bcc2)}
.job-body{position:absolute;left:138px;top:6px;width:322px}
.job-body h4{font-size:15px;font-weight:400;color:var(--orange);margin-bottom:4px}
.job-body p{font-size:13px;line-height:20px;color:#666}
.btn-view{position:absolute;left:629px;top:1674px;width:122px;height:31px;line-height:29px;text-align:center;background:var(--blue);color:#fff;font-size:15px;border-bottom:3px solid #0c5b93}

/* newsletter */
.newsletter{position:absolute;left:0;top:1821px;width:1200px;height:94px;background:var(--blue-band)}
.newsletter-label{position:absolute;left:101px;top:24px;color:#fff;font-size:19px;line-height:22px;letter-spacing:1px}
.field{position:absolute;top:30px;height:43px;background:#fff;font-size:16px;color:#aaa;padding:11px 20px;letter-spacing:.5px}
.btn-send{position:absolute;left:1007px;top:30px;width:123px;height:43px;line-height:43px;text-align:center;background:var(--orange);color:#fff;font-size:19px;letter-spacing:1px}

/* footer */
.site-footer{position:absolute;left:0;top:1915px;width:1200px;height:374px;background:var(--blue-footer);color:#fff}
.footer-heading{position:absolute;top:38px;font-size:15px;letter-spacing:1.5px;font-weight:600}
.footer-rule{position:absolute;top:71px;height:1px;background:rgba(255,255,255,.3)}
.footer-links{position:absolute;top:89px;list-style:none;font-size:13px;line-height:23px;letter-spacing:.5px}
.footer-social{position:absolute;left:108px;top:196px;display:flex;gap:6px}
.footer-social .dot{width:24px;height:24px;background:#fff}
.footer-brand{position:absolute;left:482px;top:225px;display:flex;align-items:center;gap:8px}
.footer-brand .brand-dot{width:32px;height:32px;background:#2ea6e8}
.footer-brand .brand-name{font-size:21px;color:#3fb0ee}
.location-map{position:absolute;left:819px;top:94px;width:306px;height:249px;border:4px solid #fff;background:linear-gradient(135deg,#e9e4d6,#d8d2bf 55%,#c6d4e2)}
.bottom-bar{position:absolute;left:0;top:2289px;width:1200px;height:43px;background:var(--blue-bottom);color:#fff;font-size:12px;letter-spacing:.5px;padding:13px 110px}
</style>
</head>
<body>

<header class="site-header">
  <div class="brand"><span class="brand-dot"></span><span class="brand-name">Crestway Hub</span></div>
  <div class="search">Keyword Search
    <svg width="12" height="12" viewBox="0 0 12 12"><circle cx="5" cy="5" r="3.5" fill="none" stroke="#999" stroke-width="1.4"/><line x1="7.5" y1="7.5" x2="11" y2="11" stroke="#999" stroke-width="1.4"/></svg>
  </div>
  <div class="language">Language:<span class="flag"></span></div>
  <nav class="main-nav">
    <a class="active" style="left:493px">HOME</a>
    <a style="left:601px">ABOUT</a>
    <a style="left:716px">TALENTS</a>
    <a style="left:852px">COMPANIES</a>
    <a style="left:985px">EVENTS</a>
    <a style="left:1108px">CONTACT</a>
  </nav>
</header>

<h1 class="hero-title">Crestway Hub: Linking People &amp; <span>Firms in Switzerland</span></h1>
<div class="hero-people" role="img" aria-label="Row of eight smiling professionals standing side by side, each with a colourful speech bubble naming their job"></div>

<section class="features">
  <div class="feature-grid-h"></div>
  <div class="feature-grid-h2"></div>
  <div class="feature-grid-v"></div>

  <div class="feature-icon" style="left:79px;top:142px">
    <svg width="60" height="60" viewBox="0 0 60 60" fill="#fff"><circle cx="30" cy="14" r="7"/><circle cx="15" cy="19" r="5.5"/><circle cx="45" cy="19" r="5.5"/><path d="M21 52V30a9 9 0 0 1 18 0v22z"/><path d="M8 46V32a7 7 0 0 1 11-5v19z"/><path d="M52 46V32a7 7 0 0 0-11-5v19z"/></svg>
  </div>
  <div class="feature" style="left:228px;top:136px">
    <h3>LIST OF TALENTS</h3>
    <p>Lorem ipsum dolor sit amet, consectetur adipiscing elit. Fusce vestibulum dui vitae tincidunt, a placerat ipsum feugiat. Aliquam adipiscing consectetur tellus interdum ui vitae tincidunt a placerat.</p>
    <span class="btn-more">Read more</span>
  </div>

  <div class="feature-icon" style="left:665px;top:142px">
    <svg width="60" height="60" viewBox="0 0 60 60" fill="#fff"><path d="M12 54V18l20-8v44z"/><path d="M34 54V22l14 4v28z"/><g fill="#1b82c8"><rect x="16" y="20" width="4" height="4"/><rect x="24" y="18" width="4" height="4"/><rect x="16" y="30" width="4" height="4"/><rect x="24" y="28" width="4" height="4"/><rect x="16" y="40" width="4" height="4"/><rect x="24" y="38" width="4" height="4"/><rect x="38" y="30" width="6" height="3"/><rect x="38" y="38" width="6" height="3"/></g></svg>
  </div>
  <div class="feature" style="left:810px;top:136px">
    <h3>LIST OF COMPANIES</h3>
    <p>Lorem ipsum dolor sit amet, consectetur adipiscing elit. Fusce vestibulum dui vitae tincidunt, a placerat ipsum feugiat. Aliquam adipiscing consectetur tellus interdum ui vitae tincidunt a placerat.</p>
    <span class="btn-more">Read more</span>
  </div>

  <div class="feature-icon" style="left:79px;top:390px">
    <svg width="58" height="58" viewBox="0 0 58 58"><rect x="6" y="10" width="46" height="42" rx="3" fill="#fff"/><rect x="14" y="5" width="4" height="10" rx="2" fill="#fff"/><rect x="40" y="5" width="4" height="10" rx="2" fill="#fff"/><g fill="#1b82c8"><rect x="10" y="20" width="38" height="2"/><rect x="11" y="26" width="7" height="6"/><rect x="20" y="26" width="8" height="6"/><rect x="30" y="26" width="8" height="6"/><rect x="40" y="26" width="7" height="6"/><rect x="11" y="34" width="7" height="6"/><rect x="20" y="34" width="8" height="6"/><rect x="30" y="34" width="8" height="6"/><rect x="40" y="34" width="7" height="6"/><rect x="11" y="42" width="7" height="6"/><rect x="20" y="42" width="8" height="6"/><rect x="30" y="42" width="8" height="6"/></g></svg>
  </div>
  <div class="feature" style="left:228px;top:382px">
    <h3>LATEST EVENTS</h3>
    <p>Lorem ipsum dolor sit amet, consectetur adipiscing elit. Fusce vestibulum dui vitae tincidunt, a placerat ipsum feugiat. Aliquam adipiscing consectetur tellus interdum ui vitae tincidunt a placerat.</p>
    <span class="btn-more">Read more</span>
  </div>

  <div class="feature-icon" style="left:665px;top:390px">
    <svg width="56" height="56" viewBox="0 0 56 56" fill="#fff"><path d="M6 22c0-8 10-12 22-12s22 4 22 12v4H38v-6H18v6H6z"/><path d="M14 30h28l4 16H10z"/><circle cx="28" cy="38" r="5" fill="#1b82c8"/></svg>
  </div>
  <div class="feature" style="left:810px;top:382px">
    <h3>CONTACT US</h3>
    <p>Lorem ipsum dolor sit amet, consectetur adipiscing elit. Fusce vestibulum dui vitae tincidunt, a placerat ipsum feugiat. Aliquam adipiscing consectetur tellus interdum ui vitae tincidunt a placerat.</p>
    <span class="btn-more">Read more</span>
  </div>

  <div class="feature-social"><span class="dot"></span><span class="dot" style="background:#4a8fd4"></span><span class="dot" style="background:#1a6fb0"></span></div>
</section>

<h2 class="section-heading" style="left:82px;top:1368px">WELCOME TO <span>CRESTWAY HUB</span></h2>
<div class="rule" style="left:82px;top:1408px;width:465px"></div>
<div class="welcome-text">
  <p>Lorem ipsum dolor sit amet, consectetur adipiscing elit. Phasellus eget leo leo. Sed adipiscing mi orci, vel ultrices turpis mattis a. Quisque sed eros luctus, euismod ligula et, suscipit dolor. Sed suscipit tortor eget leo hendrerit semper. Sed et fermentum erat.</p>
  <p>Curabitur tristique vestibulum bibendum. Quisque eget varius eros. Nunc id laoreet sem. Nullam vulputate fringilla mi sit amet imperdiet. Lorem ipsum dolor sit amet, consectetur adipiscing elit. Pellentesque habitant morbi tristique senectus et netus et malesuada fames ac turpis egestas.</p>
</div>

<h2 class="section-heading" style="left:625px;top:1368px">JON <span>OPENINGS</span></h2>
<div class="rule" style="left:625px;top:1408px;width:463px"></div>
<article class="job" style="top:1427px">
  <div class="job-thumb" role="img" aria-label="Presenter pointing at a growth chart in front of a seated audience"></div>
  <div class="job-body"><h4>Job title and description here</h4><p>Lorem ipsum dolor sit amet, consectetur adipiscing elit. Phasellus eget leo leo. Sed adipiscing mi orci, vel ultrices turpis mattis a.</p></div>
</article>
<article class="job" style="top:1562px">
  <div class="job-thumb" role="img" aria-label="Presenter pointing at a growth chart in front of a seated audience"></div>
  <div class="job-body"><h4>Job title and description here</h4><p>Lorem ipsum dolor sit amet, consectetur adipiscing elit. Phasellus eget leo leo. Sed adipiscing mi orci, vel ultrices turpis mattis a.</p></div>
</article>
<span class="btn-view">View All</span>

<section class="newsletter">
  <div class="newsletter-label">Join to our<br>NEWSLETTER</div>
  <div class="field" style="left:249px;width:365px">Firstname</div>
  <div class="field" style="left:628px;width:365px">Email Address</div>
  <span class="btn-send">SEND</span>
</section>

<footer class="site-footer">
  <div class="footer-heading" style="left:103px">QUICKLINKS</div>
  <div class="footer-rule" style="left:103px;width:245px"></div>
  <ul class="footer-links" style="left:108px"><li>Home</li><li>About</li><li>Talents</li><li>Companies</li></ul>
  <ul class="footer-links" style="left:249px"><li>Events</li><li>Contact</li></ul>
  <div class="footer-social"><span class="dot"></span><span class="dot"></span><span class="dot"></span><span class="dot"></span></div>

  <div class="footer-heading" style="left:480px">USEFUL INFORMATION</div>
  <div class="footer-rule" style="left:480px;width:212px"></div>
  <ul class="footer-links" style="left:488px"><li>Sitemap</li><li>F.A.Q</li><li>Privacy Policy</li><li>Terms &amp; Conditions</li></ul>
  <div class="footer-brand"><span class="brand-dot"></span><span class="brand-name">Crestway Hub</span></div>

  <div class="footer-heading" style="left:814px">LOCATION MAP</div>
  <div class="footer-rule" style="left:814px;width:320px"></div>
  <div class="location-map" role="img" aria-label="Street map of the office area with location markers"></div>
</footer>

<div class="bottom-bar">Crestway Hub Copyright 2014 &nbsp;All rights reserved</div>

</body>
</html>
```